New Webpage for one of Ireland’s largest Asian Supermarket

Introduction to Lotus Larder :

Lotus Larder is one of the largest importer, retailer, wholesaler and distributor of asian food products in Ireland. We supply to the majority of asian restaurants, shops and take-aways in Ireland.
Restaurants, caterers and shops can take advantage of our delivery service where products are delivered throughout the Republic of Ireland using our dedicated fleet of vehicles.
For more than 30 years, Lotus Larder has always adhered to the "customer first" policy sending our purchasing team to their places of origin to conduct investigations and to hire professionals to conduct assessments, to ensure that the most delicious and best quality products are provided to our customers.
Our stores stock more than 3,000 different kinds of commodities, mainly from Asia, including South Korea, Japan, mainland China, Hong Kong, Taiwan, Thailand, Malaysia and Vietnam, to meet the different tastes of our customers.

Job Description:
We would like to create a new look for our webpage in order to support multilingual feature and online shopping. The webpage can be in any CMS format, preferably pagecraft.

Our current website is:
http://lotuslarder.example/

We hope to incorporate fun and creative designs in our new website.

This design project is to develop the website design concept which will:
# Give the user confidence that Lotus Larder is a premier supermarket since 1981 and supplier to wholesalers and distributors. We provide a wide range of goods at good value.
# Inform the users of our online shopping service.
# Encourage the user to try our services.
# Looks fun, interesting, modern, respectable and trustworthy.

We are open to any fun or interesting ways of getting this message across to users.

We like the idea of real life images or cartoon based images embedded into the page similar to this:
http://www.47kites.example/
http://www.boldmaple.example/
http://www.rvorchard.example/
http://marlowe.example/club/#reception
http://www.quinnandhale.example/index.php
http://www.artmeadow.example/

We like the online shopping feature similar to this :
http://www.decotiles.example/

We like how they show their new products and brands they have at the end of their page:
http://themes.style.quv-layouts.example/?isOpen=false&;t_r=true

But, ideas could be whatever you think will look good. Any interesting concepts are welcome.

Thank you for your interest. Please do not hesitate to email brendak@lotuslarder.example should you have any queries about the contest and feel free to use any of our photos if necessary.
(our Friendspace page : https://www.facebook.com/LotusLarder.example?ref=stream )

Industry/Entity Type

Delivery Service

Requirements
Must have
• 1. Multilingual Feature (We will provide the content in different languages)
2. Online Shopping feature
3. When search in findora, links of the subpages can also be shown as well as the homepage (please see attachment for example)
4. A search engine with similar design as http://www.decotiles.example/
5. Emphasize promotion e.g. http://www.cartwell.example/WebShop/index.do#
6. Easy to manage and add new products onto the shopping page at the backend of the website
7. Friendspace and chirpline link always on the right same as http://www.boldmaple.example/
7. At least one unique feature that you think we should have on our webpage
Nice to have
• 1. Blog
2. Embedded video
3. An area, perhaps in a corner to show whether we are open and online or not. When staff are available to deliver remote support the site should clearly show that staff are online working and available now to support. When we are offline the site should also show this. ( e.g. the chatbox in http://www.boldmaple.example/)
4. A webpage adaptable to portables, mobile phones etc.
5. Memorable slogans

```html
<!DOCTYPE html>
<html lang="en">
<head>
<meta charset="utf-8">
<title>Lotus Larder – Ireland's Premium Asian Supermarket</title>
<link href="https://fonts.googleapis.com/css2?family=Open+Sans:wght@400;600;700;800&family=Oswald:wght@500;600&display=swap" rel="stylesheet">
<style>
:root{
  --yellow:#f7c600;
  --yellow-soft:#fbd84a;
  --black:#161616;
  --ink:#333;
  --grey:#777;
  --red:#c8102e;
  --orange:#f39200;
  --white:#fff;
  --line:#e2e2e2;
}
*{margin:0;padding:0;box-sizing:border-box}
html,body{width:849px;height:1200px;overflow:hidden}
body{position:relative;background:var(--yellow);font-family:"Open Sans",Arial,sans-serif;color:var(--ink);font-size:8px;line-height:1.4}
ul{list-style:none}

/* header */
.brand{position:absolute;left:84px;top:14px;display:flex;align-items:center;gap:8px}
.brand-dot{width:34px;height:34px;border-radius:50%;background:var(--red)}
.brand-name{font-weight:800;font-size:24px;color:var(--red);line-height:1}
.brand-tag{position:absolute;left:126px;top:42px;font-size:7px;font-weight:700;color:var(--black)}
.contact{position:absolute;right:82px;top:10px;display:flex;align-items:center;gap:6px}
.contact-icon{width:24px;height:24px;border-radius:50%;background:var(--black);display:flex;align-items:center;justify-content:center}
.contact-text{text-align:right}
.contact-phone{font-family:"Oswald",sans-serif;font-size:15px;color:var(--white);background:var(--black);padding:0 6px;border-radius:3px}
.contact-mail{font-weight:700;font-size:10px;color:var(--black)}
.main-nav{position:absolute;left:334px;top:58px;height:30px;display:flex;background:var(--black);border-radius:3px 3px 0 0;overflow:hidden}
.main-nav a{color:var(--white);text-decoration:none;font-size:10px;font-weight:600;padding:0 15px;line-height:30px}
.main-nav a.active{background:var(--yellow);color:var(--black)}

/* hero */
.hero{position:absolute;left:80px;top:92px;width:690px;height:250px;background:var(--white);padding:6px}
.hero-photo{width:100%;height:100%;background:linear-gradient(110deg,#e9eef2 0%,#c7d3dc 35%,#e7b7a2 55%,#d8dfe4 75%,#f2f2ee 100%)}

/* social rail */
.social{position:absolute;left:0;top:372px;display:flex;flex-direction:column;gap:2px}
.social span{width:26px;height:26px;background:var(--black);color:var(--white);font-size:9px;font-weight:700;display:flex;align-items:center;justify-content:center}

/* content panel */
.panel{position:absolute;left:80px;top:342px;width:690px;height:668px;background:var(--white)}

.categories{position:absolute;left:8px;top:14px;width:140px;background:var(--yellow);padding:14px 10px;border-radius:3px}
.categories li{font-size:8px;color:var(--black);padding:3.5px 0 3.5px 10px;position:relative;border-bottom:1px solid rgba(0,0,0,.08)}
.categories li::before{content:"";position:absolute;left:0;top:8px;width:4px;height:4px;border-radius:50%;background:var(--black)}

.fan-box{position:absolute;left:8px;top:332px;width:140px;height:176px;border:1px solid var(--line);padding:8px;font-size:7px}
.fan-head{display:flex;gap:6px;align-items:center}
.fan-thumb{width:30px;height:30px;background:var(--yellow)}
.fan-name{font-weight:700;font-size:9px;color:var(--black)}
.fan-like{display:inline-block;margin-top:3px;border:1px solid #bbb;padding:0 5px;font-size:7px;background:#f3f3f3}
.fan-post{margin-top:10px;border-top:1px solid var(--line);padding-top:6px;color:var(--grey)}
.fan-post b{color:var(--black)}
.fan-post-img{margin-top:6px;height:52px;background:linear-gradient(135deg,#c9a56d,#8c6a3e)}

.side-feature{position:absolute;left:8px;top:516px;width:140px}
.side-feature-photo{height:118px;background:linear-gradient(160deg,#e9d6b8,#b98f5c 60%,#6f5435)}
.side-feature p{font-size:7px;color:var(--black);margin-top:4px}

.welcome{position:absolute;left:176px;top:16px;width:506px}
.welcome h1{font-size:13px;font-weight:700;color:var(--black)}
.welcome h1 em{font-style:normal;color:var(--red)}
.welcome .lead{color:var(--red);font-size:7px;margin-top:4px;font-weight:600}
.welcome-row{display:flex;gap:10px;margin-top:8px}
.welcome-photo{width:82px;height:68px;flex:none;background:linear-gradient(135deg,#d7c8b1,#9a8467)}
.welcome-row p{font-size:7.5px;color:var(--grey)}
.welcome-row p b{color:var(--black)}
.welcome .more{font-size:7.5px;color:var(--grey);margin-top:10px}

.section-title{position:absolute;left:176px;display:flex;align-items:center;gap:6px;font-family:"Oswald",sans-serif;font-size:15px;color:var(--black)}
.section-title em{font-style:normal;color:var(--orange)}
.promo-title{top:218px;width:506px;height:28px;background:linear-gradient(90deg,var(--yellow-soft),#fff 70%);padding-left:8px;border-radius:14px 0 0 14px}
.promo-badge{width:20px;height:20px;border-radius:50%;background:var(--orange)}

.products{position:absolute;left:176px;top:258px;width:506px;display:flex;justify-content:space-between}
.product{width:116px}
.product-photo{height:64px;margin:0 14px 6px;background:linear-gradient(180deg,#f1f1f1,#cfd6dc)}
.product-name{font-size:6.5px;color:var(--grey);line-height:1.3}
.product-price{font-family:"Oswald",sans-serif;font-size:14px;color:var(--orange);line-height:1.3}
.product-was{font-size:6.5px;color:var(--grey);text-decoration:line-through}

.news-title{top:398px}
.news-icon{width:24px;height:24px;border-radius:50%;background:var(--orange)}
.news-title em{color:var(--orange)}
.posts{position:absolute;left:176px;top:434px;width:506px}
.post{display:flex;gap:10px;padding:8px 0;border-bottom:1px solid var(--line)}
.post-photo{width:82px;height:64px;flex:none;background:linear-gradient(135deg,#c7a27a,#7e5a3c)}
.post:nth-child(2) .post-photo{background:linear-gradient(135deg,#e1c46a,#a2782f)}
.post h3{font-size:9.5px;font-weight:600;color:var(--black)}
.post p{font-size:7px;color:var(--grey);margin-top:3px}
.post .meta{font-size:6.5px;color:var(--red);text-align:right;margin-top:5px}

/* footer */
.footer{position:absolute;left:0;top:1010px;width:849px;height:165px;background:var(--black);padding:16px 80px 0}
.footer-cols{display:flex;justify-content:space-between}
.footer-col h4{font-size:12px;font-weight:700;color:var(--white);margin-bottom:8px}
.footer-col h4 em{font-style:normal;color:var(--yellow)}
.footer-col li{font-size:8px;color:#cfcfcf;padding:2.5px 0 2.5px 10px;position:relative}
.footer-col li::before{content:"";position:absolute;left:0;top:7px;width:4px;height:4px;background:var(--yellow)}
.bottom-bar{position:absolute;left:0;top:1175px;width:849px;height:25px;background:var(--yellow);display:flex;justify-content:space-between;align-items:center;padding:0 80px;font-size:7.5px;color:var(--black)}
.bottom-bar nav a{color:var(--black);text-decoration:none;margin-right:4px}
</style>
</head>
<body>

<header>
  <div class="brand"><span class="brand-dot"></span><span class="brand-name">Lotus Larder</span></div>
  <div class="brand-tag">Ireland's Premium Asian Supermarket · Since 1981</div>
  <div class="contact">
    <div class="contact-text">
      <div class="contact-phone">061 555 0192</div>
      <div class="contact-mail">Email Us</div>
    </div>
    <div class="contact-icon">
      <svg width="12" height="12" viewBox="0 0 24 24"><path fill="#f7c600" d="M6.6 10.8a15 15 0 0 0 6.6 6.6l2.2-2.2c.3-.3.7-.4 1-.2 1.1.4 2.3.6 3.6.6.6 0 1 .4 1 1V20c0 .6-.4 1-1 1A17 17 0 0 1 3 4c0-.6.4-1 1-1h3.5c.6 0 1 .4 1 1 0 1.3.2 2.5.6 3.6.1.3 0 .7-.2 1z"/></svg>
    </div>
  </div>
  <nav class="main-nav">
    <a class="active" href="#">Home</a><a href="#">About Us</a><a href="#">Products</a><a href="#">Our Stores</a><a href="#">Events</a><a href="#">Contacts</a>
  </nav>
</header>

<div class="hero"><div class="hero-photo" role="img" aria-label="Smiling shop assistant in a bright supermarket aisle stocked with Asian groceries"></div></div>

<div class="social" aria-label="Social links">
  <span title="chirpline">C</span><span title="Friendspace">F</span><span title="pagecraft">P</span><span title="findora">F+</span>
</div>

<main class="panel">
  <aside>
    <ul class="categories">
      <li>Confectionery</li><li>Dairy &amp; Eggs</li><li>Bakery</li><li>Fresh Food</li><li>Chilled Food</li><li>Frozen Food</li><li>Household / Health</li><li>Organic Food</li><li>Baby Care</li><li>Personal Care</li><li>Pet Care</li><li>General Merchandise</li>
    </ul>
    <div class="fan-box">
      <div class="fan-head"><div class="fan-thumb"></div><div><div class="fan-name">Lotus Larder</div><span class="fan-like">Like</span></div></div>
      <div class="fan-post"><b>Lotus Larder</b> Time for a coffee break? Fresh roast and sweet buns in store today.
        <div class="fan-post-img" role="img" aria-label="Coffee and pastries photo"></div></div>
    </div>
    <div class="side-feature">
      <div class="side-feature-photo" role="img" aria-label="Customer browsing the snack shelves"></div>
      <p>Bramble Baby Bites Fruit Teething Set – Lime and Green 3 Pack</p>
    </div>
  </aside>

  <section class="welcome">
    <h1>Welcome to <em>Lotus Larder !!</em></h1>
    <p class="lead">Fresh Asian groceries, weekly imports and trusted wholesale supply for shops, caterers and restaurants across Ireland.</p>
    <div class="welcome-row">
      <div class="welcome-photo" role="img" aria-label="Storefront with shelves of imported goods"></div>
      <p><b>Lorem ipsum dolor sit amet, consectetur</b> adipiscing elit. Donec libero. Suspendisse bibendum. Cras id urna. Morbi tincidunt, orci ac convallis aliquam, lectus turpis varius lorem, eu posuere nunc justo tempus leo. Donec mattis, purus nec placerat bibendum, dui pede condimentum odio, ac placerat tellus lorem quis tortor.</p>
    </div>
    <p class="more">Lorem ipsum dolor sit amet, consectetuer adipiscing elit. Donec libero. Suspendisse bibendum. Cras id urna. Sed felis ipsum, vulputate bibendum, semper quis, hendrerit sed felis.</p>
  </section>

  <h2 class="section-title promo-title"><span class="promo-badge"></span>Latest <em>Promotion</em></h2>
  <div class="products">
    <div class="product"><div class="product-photo" role="img" aria-label="Packaged snack box"></div><p class="product-name">Bramble Baby Bites Fruit Teething Set – Lime and Green</p><p class="product-price">Today $6.00</p><p class="product-was">$8.00 Was</p></div>
    <div class="product"><div class="product-photo" role="img" aria-label="Tub of skin cream"></div><p class="product-name">Bramble Baby Bites Fruit Teething Set – Lime and Green</p><p class="product-price">Today $6.00</p><p class="product-was">$8.00 Was</p></div>
    <div class="product"><div class="product-photo" role="img" aria-label="Bottle of hair care"></div><p class="product-name">Bramble Baby Bites Fruit Teething Set – Lime and Green</p><p class="product-price">Today $6.00</p><p class="product-was">$8.00 Was</p></div>
    <div class="product"><div class="product-photo" role="img" aria-label="Cosmetics gift pack"></div><p class="product-name">Bramble Baby Bites Fruit Teething Set – Lime and Green</p><p class="product-price">Today $6.00</p><p class="product-was">$8.00 Was</p></div>
  </div>

  <h2 class="section-title news-title"><span class="news-icon"></span>News <em>&amp; Blog</em></h2>
  <div class="posts">
    <article class="post"><div class="post-photo" role="img" aria-label="Shopper in a grocery aisle"></div><div><h3>Plexa Suggests Advertisers Are Overpaying For Display Ads</h3><p>No one would happily pay full price for 2 kinds of anything. So what happens when data shows many advertisers have been doing exactly that with hundreds of millions of online ad spend for years?</p><p class="meta">Posted by Lotus Larder | 12-11-2013</p></div></article>
    <article class="post"><div class="post-photo" role="img" aria-label="Fresh produce display"></div><div><h3>Plexa Suggests Advertisers Are Overpaying For Display Ads</h3><p>No one would happily pay full price for 2 kinds of anything. So what happens when data shows many advertisers have been doing exactly that with hundreds of millions of online ad spend for years?</p><p class="meta">Posted by Lotus Larder | 12-11-2013</p></div></article>
  </div>
</main>

<footer class="footer">
  <div class="footer-cols">
    <div class="footer-col"><h4>Shop <em>Online</em></h4><ul><li>Quick Tour</li><li>No Worries Guarantee</li><li>Delivery Fees</li><li>Common Questions</li></ul></div>
    <div class="footer-col"><h4><em>Financial</em> Services</h4><ul><li>The Flower Gallery</li><li>Fulfilment</li><li>Baby &amp; Toddler Care</li><li>Online Marketplace</li></ul></div>
    <div class="footer-col"><h4><em>Other</em> Brands</h4><ul><li>Quick Tour</li><li>No Worries Guarantee</li><li>Delivery Fees</li><li>Common Questions</li></ul></div>
    <div class="footer-col"><h4>Fresh <em>Ideas</em></h4><ul><li>Quick Tour</li><li>No Worries Guarantee</li><li>Delivery Fees</li><li>Common Questions</li></ul></div>
  </div>
</footer>
<div class="bottom-bar">
  <nav><a href="#">Home</a>| <a href="#">About Us</a>| <a href="#">Products</a>| <a href="#">Our Stores</a>| <a href="#">Events</a>| <a href="#">Contacts</a></nav>
  <span>© 2013 lotuslarder | All Rights Reserved</span>
</div>

</body>
</html>
```